Business Card Design - Bluewater Harbor Financial Services, Inc.

Name Darnell Ashcombe Title Mortgage Originator
Location (800) 417-6290 x31 Since 2021
Direct (240) 715-4426 Email dashcombe@bluewaterharborhome.com
NMLS 3860472 Licensed MD
www.bluewaterharborhome.com
Name Rosalind Mae Tharp Title Mortgage Originator
Location (800) 417-6290 x32 Since 2021
Direct (443) 691-7254 Email rtharp@bluewaterharborhome.com
NMLS 3867915 Licensed MD
www.bluewaterharborhome.com
Name Marcus Odell Pruitt Title Mortgage Originator
Location (800) 417-6290 x64 Since 2021
Direct (240) 347-1965 Email mpruitt@bluewaterharborhome.com
NMLS 3894107 Licensed MD
www.bluewaterharborhome.com
Name Dale Hensick Title Mortgage Originator
Location (800) 417-6290 x30 Since 2021
Direct (240) 529-6078 Email dhensick@bluewaterharborhome.com
NMLS 4538960 Licensed MD,VA
www.bluewaterharborhome.com
Name Owen Calder Title Mortgage Originator
Location (800) 417-6290 x33 Since 2021
Direct (240) 529-6078 Email ocalder@bluewaterharborhome.com
NMLS 3869354 Licensed MD
www.bluewaterharborhome.com
Contact Information for Business Card
Name Darnell Ashcombe Title Mortgage Originator Location (800) 417-6290 x31 Since 2021 Direct (240) 715-4426 Email dashcombe@bluewaterharborhome.com NMLS 3860472 Licensed MD www.bluewaterharborhome.com Name Rosalind Mae Tharp Title Mortgage Originator Location (800) 417-6290 x32 Since 2021 Direct (443) 691-7254 Email rtharp@bluewaterharborhome.com NMLS 3867915 Licensed MD www.bluewaterharborhome.com Name Marcus Odell Pruitt Title Mortgage Originator Location (800) 417-6290 x64 Since 2021 Direct (240) 347-1965 Email mpruitt@bluewaterharborhome.com NMLS 3894107 Licensed MD www.bluewaterharborhome.com Name Dale Hensick Title Mortgage Originator Location (800) 417-6290 x30 Since 2021 Direct (240) 529-6078 Email dhensick@bluewaterharborhome.com NMLS 4538960 Licensed MD,VA www.bluewaterharborhome.com Name Owen Calder Title Mortgage Originator Location (800) 417-6290 x33 Since 2021 Direct (240) 529-6078 Email ocalder@bluewaterharborhome.com NMLS 3869354 Licensed MD www.bluewaterharborhome.com

```html
<!DOCTYPE html>
<html lang="en">
<head>
<meta charset="utf-8">
<title>Bluewater Harbor Financial Services – Business Cards</title>
<link rel="stylesheet" href="https://fonts.googleapis.com/css2?family=Montserrat:wght@500;600;700;800&display=swap">
<style>
  :root{
    --sky:#1e9ad6;
    --navy:#0c4f8f;
    --deep:#0a63a8;
    --gold:#c9b875;
    --ink:#1d1d1f;
    --paper:#ffffff;
    --bg:#ffffff;
  }
  *{box-sizing:border-box;margin:0;padding:0}
  html,body{width:1200px;height:1200px;overflow:hidden;background:var(--bg)}
  body{position:relative;font-family:"Montserrat",Arial,sans-serif;color:var(--ink)}

  .card{position:absolute;width:468px;height:267px;background:var(--paper);
        box-shadow:0 1px 4px rgba(0,0,0,.28);overflow:hidden}
  .card .band{position:absolute;left:0;top:0;width:468px;height:267px}

  .brand{position:absolute;left:58px;top:30px;width:160px;height:54px;display:flex;align-items:center;gap:9px}
  .brand-dot{flex:none;width:32px;height:32px;border-radius:50%;background:var(--gold)}
  .brand-name{font-weight:700;color:var(--navy);font-size:12px;line-height:1.3}

  .portrait{position:absolute;left:298px;top:10px;width:100px;height:100px;border-radius:50%;
            border:2px solid var(--navy);background:radial-gradient(circle at 50% 40%,#8a6a55,#3a3a44)}

  .identity{position:absolute;right:23px;top:117px;text-align:right}
  .name{font-weight:800;color:var(--sky);font-size:20px;line-height:20px;text-transform:uppercase;white-space:nowrap}
  .role{font-weight:700;color:var(--navy);font-size:15.5px;line-height:18px;margin-top:2px}
  .license{font-weight:500;font-size:11px;line-height:14px;margin-top:2px;white-space:nowrap}

  .contacts{position:absolute;left:24px;top:132px;list-style:none}
  .contacts li{display:flex;align-items:center;gap:9px;height:19.5px;font-size:11px;font-weight:500;white-space:nowrap}
  .contacts svg{width:13px;height:13px;flex:none;fill:var(--sky)}

  .web{position:absolute;left:30px;top:230px;display:flex;align-items:center;gap:12px;
       color:#fff;font-weight:600;font-size:14px;letter-spacing:.2px}
  .web svg{width:22px;height:22px}

  /* front card */
  .front .brand{left:128px;top:82px;width:220px;height:60px;gap:12px}
  .front .brand-dot{width:46px;height:46px}
  .front .brand-name{font-size:16px}
  .social{position:absolute;left:72px;top:208px;width:320px;height:59px;background:var(--sky);
          border-radius:8px 8px 0 0;display:flex;align-items:center;gap:12px;padding-left:22px;
          color:#fff;font-weight:600;font-size:12px;white-space:nowrap}
  .social-dot{width:26px;height:26px;border-radius:50%;background:#fff;flex:none}
</style>
</head>
<body>

<svg width="0" height="0" style="position:absolute">
  <defs>
    <symbol id="i-phone" viewBox="0 0 24 24"><path d="M6.6 10.8a15.1 15.1 0 0 0 6.6 6.6l2.2-2.2c.3-.3.7-.4 1-.2 1.1.4 2.3.6 3.6.6.6 0 1 .4 1 1V20c0 .6-.4 1-1 1A17 17 0 0 1 3 4c0-.6.4-1 1-1h3.5c.6 0 1 .4 1 1 0 1.3.2 2.5.6 3.6.1.3 0 .7-.2 1z"/></symbol>
    <symbol id="i-mail" viewBox="0 0 24 24"><path d="M2 5h20v14H2zM4 7v10h16V7l-8 6z"/></symbol>
    <symbol id="i-home" viewBox="0 0 24 24"><path d="M12 3 1 12h3v9h6v-6h4v6h6v-9h3z"/></symbol>
    <symbol id="i-globe" viewBox="0 0 24 24"><g fill="none" stroke="#fff" stroke-width="1.6"><circle cx="12" cy="12" r="10"/><ellipse cx="12" cy="12" rx="4.5" ry="10"/><path d="M2 12h20M4 6.5h16M4 17.5h16"/></g></symbol>
    <symbol id="card-band" viewBox="0 0 468 267">
      <polygon points="0,214 468,194 468,267 0,267" fill="#1e9ad6"/>
      <line x1="0" y1="202" x2="468" y2="182" stroke="#0c4f8f" stroke-width="3.5"/>
      <line x1="0" y1="209" x2="468" y2="189" stroke="#0c4f8f" stroke-width="2"/>
    </symbol>
  </defs>
</svg>

<!-- Front -->
<section class="card front" style="left:368px;top:8px">
  <svg class="band" viewBox="0 0 468 267">
    <polygon points="0,258 72,226 72,267 0,267" fill="#0a63a8"/>
    <polygon points="468,258 392,226 392,267 468,267" fill="#0a63a8"/>
  </svg>
  <div class="brand"><span class="brand-dot"></span><span class="brand-name">Bluewater Harbor Financial Services, Inc.</span></div>
  <div class="social"><span class="social-dot"></span>BLUEWATERHARBORHOME.COM/SOCIAL</div>
</section>

<!-- Darnell Ashcombe -->
<section class="card" style="left:118px;top:314px">
  <svg class="band"><use href="#card-band"/></svg>
  <div class="brand"><span class="brand-dot"></span><span class="brand-name">Bluewater Harbor Financial Services, Inc.</span></div>
  <div class="portrait" role="img" aria-label="Portrait photo of Darnell Ashcombe"></div>
  <div class="identity"><p class="name">Darnell Ashcombe</p><p class="role">Mortgage Originator</p><p class="license">NMLS 3860472 Licensed MD</p></div>
  <ul class="contacts">
    <li><svg><use href="#i-phone"/></svg>(240) 715-4426</li>
    <li><svg><use href="#i-mail"/></svg>dashcombe@bluewaterharborhome.com</li>
    <li><svg><use href="#i-home"/></svg>(800) 417-6290 x31 Since 2021</li>
  </ul>
  <div class="web"><svg><use href="#i-globe"/></svg>WWW.BLUEWATERHARBORHOME.COM</div>
</section>

<!-- Rosalind Mae Tharp -->
<section class="card" style="left:616px;top:314px">
  <svg class="band"><use href="#card-band"/></svg>
  <div class="brand"><span class="brand-dot"></span><span class="brand-name">Bluewater Harbor Financial Services, Inc.</span></div>
  <div class="portrait" role="img" aria-label="Portrait photo of Rosalind Mae Tharp"></div>
  <div class="identity"><p class="name">Rosalind Mae Tharp</p><p class="role">Mortgage Originator</p><p class="license">NMLS 3867915 Licensed MD</p></div>
  <ul class="contacts">
    <li><svg><use href="#i-phone"/></svg>(443) 691-7254</li>
    <li><svg><use href="#i-mail"/></svg>rtharp@bluewaterharborhome.com</li>
    <li><svg><use href="#i-home"/></svg>(800) 417-6290 x32 Since 2021</li>
  </ul>
  <div class="web"><svg><use href="#i-globe"/></svg>WWW.BLUEWATERHARBORHOME.COM</div>
</section>

<!-- Marcus Odell Pruitt -->
<section class="card" style="left:118px;top:617px">
  <svg class="band"><use href="#card-band"/></svg>
  <div class="brand"><span class="brand-dot"></span><span class="brand-name">Bluewater Harbor Financial Services, Inc.</span></div>
  <div class="portrait" role="img" aria-label="Portrait photo of Marcus Odell Pruitt"></div>
  <div class="identity"><p class="name">Marcus Odell Pruitt</p><p class="role">Mortgage Originator</p><p class="license">NMLS 3894107 Licensed MD</p></div>
  <ul class="contacts">
    <li><svg><use href="#i-phone"/></svg>(240) 347-1965</li>
    <li><svg><use href="#i-mail"/></svg>mpruitt@bluewaterharborhome.com</li>
    <li><svg><use href="#i-home"/></svg>(800) 417-6290 x64 Since</li>
  </ul>
  <div class="web"><svg><use href="#i-globe"/></svg>WWW.BLUEWATERHARBORHOME.COM</div>
</section>

<!-- Dale Hensick -->
<section class="card" style="left:616px;top:617px">
  <svg class="band"><use href="#card-band"/></svg>
  <div class="brand"><span class="brand-dot"></span><span class="brand-name">Bluewater Harbor Financial Services, Inc.</span></div>
  <div class="portrait" role="img" aria-label="Portrait photo of Dale Hensick"></div>
  <div class="identity"><p class="name">Dale Hensick</p><p class="role">Mortgage Originator</p><p class="license">NMLS 4538960 Licensed MD,VA</p></div>
  <ul class="contacts">
    <li><svg><use href="#i-phone"/></svg>(240) 529-6078</li>
    <li><svg><use href="#i-mail"/></svg>dhensick@bluewaterharborhome.com</li>
    <li><svg><use href="#i-home"/></svg>(800) 417-6290 x30 Since 2021</li>
  </ul>
  <div class="web"><svg><use href="#i-globe"/></svg>WWW.BLUEWATERHARBORHOME.COM</div>
</section>

<!-- Owen Calder -->
<section class="card" style="left:364px;top:924px">
  <svg class="band"><use href="#card-band"/></svg>
  <div class="brand"><span class="brand-dot"></span><span class="brand-name">Bluewater Harbor Financial Services, Inc.</span></div>
  <div class="portrait" role="img" aria-label="Portrait photo of Owen Calder"></div>
  <div class="identity"><p class="name">Owen Calder</p><p class="role">Mortgage Originator</p><p class="license">NMLS 3869354 Licensed MD</p></div>
  <ul class="contacts">
    <li><svg><use href="#i-phone"/></svg>(240) 529-6078</li>
    <li><svg><use href="#i-mail"/></svg>ocalder@bluewaterharborhome.com</li>
    <li><svg><use href="#i-home"/></svg>(800) 417-6290 x33 Since 2021</li>
  </ul>
  <div class="web"><svg><use href="#i-globe"/></svg>WWW.BLUEWATERHARBORHOME.COM</div>
</section>

</body>
</html>
```